Accountancy firm needs clean and simple website and optional logo

We need a logo and basic wordpress website design for a Sydney based accountancy firm.
We need a clean and simple logo and website, based on the accounting/finance/tax industry. Simple, credible and official colors.
The logo is expected to be so simple that we have combined into the one job.
If you submit a logo design and we choose it along with someone else's website design you will be paid a bonus of $60. The website design will still win the competition as per normal.
Current website is old and terrible but gives you an idea of the sitemap (super simple) and what they do: www.brookfiscal.com.au
We want original different to normal template looking designs.
We like videos, and like http://www.whitfords.com.au/
Feel free to go to vidhaven and use some videos from there.
We are based in Sydney Australia and in the field of taxation and accounting
We want a clean, formal, credible site, limited pages.
The project is guaranteed, so go for it.
Brook & Associates
1 page

```html
<!DOCTYPE html>
<html lang="en">
<head>
<meta charset="utf-8">
<title>Brook &amp; Associates — Tax Accountants</title>
<link rel="stylesheet" href="https://fonts.googleapis.com/css2?family=Montserrat:wght@400;500;600;700&display=swap">
<style>
:root{
  --blue-top:#0fb0f5;
  --blue-bottom:#0a7ddb;
  --accent:#16a6ee;
  --ink:#222222;
  --muted:#8a8a8a;
  --light-band:#f2f2f2;
  --mid-band:#d9d9d9;
  --dark-band:#3d3d3d;
  --footer:#262626;
  --white:#ffffff;
  --field:rgba(255,255,255,.28);
}
*{box-sizing:border-box;margin:0;padding:0}
html,body{width:1200px;height:3140px;overflow:hidden}
body{font-family:"Montserrat",sans-serif;color:var(--ink);background:var(--white);position:relative}
section,header,footer{position:absolute;left:0;width:1200px}

/* Hero */
.hero{top:0;height:690px;background:linear-gradient(180deg,var(--blue-top),var(--blue-bottom));color:var(--white);text-align:center}
.brand{position:absolute;left:88px;top:64px;font-size:17px;font-weight:600;letter-spacing:.3px;line-height:1;color:var(--white);white-space:nowrap}
.nav{position:absolute;right:70px;top:62px;display:flex;gap:58px;font-size:17px;font-weight:500}
.hero-title{position:absolute;top:255px;width:100%;font-size:72px;font-weight:700;line-height:62px}
.hero-sub{position:absolute;top:388px;width:100%;font-size:15px}
.hero-btn{position:absolute;left:488px;top:425px;width:220px;height:40px;border-radius:20px;background:linear-gradient(#ffffff,#dcdcdc);color:#7a7a7a;font-size:20px;line-height:40px}
.dots{position:absolute;top:593px;left:565px;display:flex;gap:8px}
.dots span{width:16px;height:16px;border:2px solid var(--white);border-radius:50%}

/* Shared */
.section-title{position:absolute;width:100%;text-align:center;font-weight:600;color:var(--ink)}
.section-sub{position:absolute;width:100%;text-align:center;color:var(--muted)}
.col{position:absolute;text-align:center}
.col h3{font-weight:600;text-transform:uppercase}
.col p{color:var(--muted)}

/* Intro */
.intro{top:690px;height:505px;background:var(--white)}
.intro .section-title{top:105px;font-size:24px}
.intro .section-sub{top:136px;font-size:12px}
.intro .col{top:220px;width:220px}
.intro .col h3{font-size:17px;font-weight:500;margin-bottom:12px}
.intro .col p{font-size:12px;line-height:18px}

/* Services */
.services{top:1195px;height:475px;background:var(--light-band)}
.services .section-title{top:92px;font-size:31px}
.services .section-sub{top:135px;font-size:14px}
.services .col{top:210px;width:230px}
.tile{width:62px;height:62px;margin:0 auto 20px;border-radius:6px;display:block}
.services .col h3,.culture .col h3{font-size:13px;margin-bottom:10px}
.services .col p,.culture .col p{font-size:10.5px;line-height:15px}

/* Culture */
.culture{top:1670px;height:530px;background:var(--mid-band)}
.culture .section-title{top:110px;font-size:31px}
.culture .section-sub{top:153px;font-size:14px}
.culture .link-line{position:absolute;top:274px;height:3px;background:#a8a8a8}
.culture .col{top:228px;width:230px}
.badge{width:92px;height:92px;margin:0 auto 16px;display:block}

/* Call */
.call{top:2200px;height:280px;background:var(--dark-band);color:var(--white);text-align:center}
.call-icon{position:absolute;left:553px;top:-28px;width:94px;height:94px}
.call h2{position:absolute;top:105px;width:100%;font-size:33px;font-weight:600}
.call-number{position:absolute;top:170px;width:100%;font-size:44px;font-weight:400}

/* Contact */
.contact{top:2480px;height:535px;background:linear-gradient(180deg,var(--blue-top),var(--blue-bottom));color:var(--white)}
.contact .section-title{top:60px;font-size:27px;color:var(--white)}
.contact .section-sub{top:90px;font-size:12px;color:var(--white)}
.field{position:absolute;left:333px;width:532px;background:var(--field);color:rgba(255,255,255,.75);font-size:13px;padding:12px 20px}
.field.name{top:146px;height:48px}
.field.email{top:206px;height:48px}
.field.message{top:266px;height:134px}
.send-btn{position:absolute;left:508px;top:432px;width:180px;height:38px;border-radius:19px;background:linear-gradient(#ffffff,#dcdcdc);color:var(--ink);font-size:16px;font-weight:500;text-align:center;line-height:38px}

/* Footer */
.footer{top:3015px;height:125px;background:var(--footer);color:var(--white)}
.footer .brand{left:140px;top:46px}
.social{position:absolute;right:150px;top:38px;display:flex;gap:14px}
.social span{width:42px;height:42px;border-radius:50%;background:#d8d8d8;display:block}
</style>
</head>
<body>

<header class="hero">
  <div class="brand">Brook &amp; Associates</div>
  <nav class="nav"><span>HOME</span><span>ABOUT</span><span>BLOG</span><span>CONTACT</span></nav>
  <h1 class="hero-title">LOREM IPSUM<br>DOLOR</h1>
  <p class="hero-sub">Proin iaculis purus consequat sem cure.</p>
  <div class="hero-btn">Proin iaculis</div>
  <div class="dots"><span></span><span></span><span></span></div>
</header>

<section class="intro">
  <h2 class="section-title">SUSPENDISSE POTENTI</h2>
  <p class="section-sub">Lorem ipsum dolor sit amet</p>
  <div class="col" style="left:122px"><h3>Praesent varius</h3><p>Lorem ipsum dolor sit amet consectetur adipiscing elit. Morbi vel elementum augue. In hac habitasse platea dictumst. Sed ullamcorper ante quam, eu fringilla est elementum sit amet. Vestibulum non ligula neque.</p></div>
  <div class="col" style="left:367px"><h3>Donec</h3><p>Lorem ipsum dolor sit amet consectetur adipiscing elit. Morbi vel elementum augue. In hac habitasse platea dictumst. Sed ullamcorper ante quam, eu fringilla est elementum sit amet. Vestibulum non ligula neque.</p></div>
  <div class="col" style="left:612px"><h3>Sed pretium</h3><p>Lorem ipsum dolor sit amet consectetur adipiscing elit. Morbi vel elementum augue. In hac habitasse platea dictumst. Sed ullamcorper ante quam, eu fringilla est elementum sit amet. Vestibulum non ligula neque.</p></div>
  <div class="col" style="left:857px"><h3>Integer a ante</h3><p>Lorem ipsum dolor sit amet consectetur adipiscing elit. Morbi vel elementum augue. In hac habitasse platea dictumst. Sed ullamcorper ante quam, eu fringilla est elementum sit amet. Vestibulum non ligula neque.</p></div>
</section>

<section class="services">
  <h2 class="section-title">PROFESSIONAL SERVICES</h2>
  <p class="section-sub">Proin iaculis purus consequat sem cure</p>
  <div class="col" style="left:212px">
    <svg class="tile" viewBox="0 0 62 62"><rect width="62" height="62" rx="6" fill="#16a6ee"/><rect x="15" y="11" width="32" height="40" rx="3" fill="none" stroke="#fff" stroke-width="3"/><rect x="20" y="16" width="22" height="7" fill="#fff"/><g fill="#fff"><rect x="20" y="27" width="5" height="5"/><rect x="28.5" y="27" width="5" height="5"/><rect x="37" y="27" width="5" height="5"/><rect x="20" y="35" width="5" height="5"/><rect x="28.5" y="35" width="5" height="5"/><rect x="37" y="35" width="5" height="5"/><rect x="20" y="43" width="5" height="4"/><rect x="28.5" y="43" width="5" height="4"/><rect x="37" y="43" width="5" height="4"/></g></svg>
    <h3>Beautiful designs</h3><p>Proin iaculis purus consequat sem cure dignissim. Donec porttitor entum suscipit aenean rhoncus posuere elit in tincidunt.</p>
  </div>
  <div class="col" style="left:485px">
    <svg class="tile" viewBox="0 0 62 62"><rect width="62" height="62" rx="6" fill="#16a6ee"/><rect x="14" y="12" width="34" height="38" rx="3" fill="none" stroke="#fff" stroke-width="3"/><g stroke="#fff" stroke-width="3"><line x1="19" y1="21" x2="43" y2="21"/><line x1="19" y1="28" x2="43" y2="28"/><line x1="19" y1="35" x2="43" y2="35"/><line x1="19" y1="42" x2="43" y2="42"/></g></svg>
    <h3>Responsive web</h3><p>Proin iaculis purus consequat sem cure dignissim. Donec porttitor entum suscipit aenean rhoncus posuere elit in tincidunt.</p>
  </div>
  <div class="col" style="left:758px">
    <svg class="tile" viewBox="0 0 62 62"><rect width="62" height="62" rx="6" fill="#16a6ee"/><rect x="12" y="12" width="38" height="38" fill="none" stroke="#fff" stroke-width="3"/><polyline points="16,44 26,32 33,38 45,22" fill="none" stroke="#fff" stroke-width="3.5"/></svg>
    <h3>Marketing tools</h3><p>Proin iaculis purus consequat sem cure dignissim. Donec porttitor entum suscipit aenean rhoncus posuere elit in tincidunt.</p>
  </div>
</section>

<section class="culture">
  <h2 class="section-title">CULTURE &amp; VALUES</h2>
  <p class="section-sub">Proin iaculis purus consequat sem cure</p>
  <div class="link-line" style="left:382px;width:172px"></div>
  <div class="link-line" style="left:646px;width:172px"></div>
  <div class="col" style="left:212px">
    <svg class="badge" viewBox="0 0 92 92"><circle cx="46" cy="46" r="42" fill="#fff" stroke="#5a5a5a" stroke-width="6"/><rect x="33" y="28" width="26" height="34" rx="2" fill="none" stroke="#5a5a5a" stroke-width="3"/><rect x="37" y="32" width="18" height="6" fill="#5a5a5a"/><g fill="#5a5a5a"><rect x="37" y="42" width="4" height="4"/><rect x="44" y="42" width="4" height="4"/><rect x="51" y="42" width="4" height="4"/><rect x="37" y="49" width="4" height="4"/><rect x="44" y="49" width="4" height="4"/><rect x="51" y="49" width="4" height="4"/><rect x="37" y="55" width="4" height="3"/><rect x="44" y="55" width="4" height="3"/><rect x="51" y="55" width="4" height="3"/></g></svg>
    <h3>Work-life balance</h3><p>Proin iaculis purus consequat sem cure dignissim. Donec porttitor entum suscipit aenean rhoncus posuere elit in tincidunt.</p>
  </div>
  <div class="col" style="left:485px">
    <svg class="badge" viewBox="0 0 92 92"><circle cx="46" cy="46" r="42" fill="#fff" stroke="#5a5a5a" stroke-width="6"/><rect x="30" y="28" width="32" height="34" rx="3" fill="none" stroke="#5a5a5a" stroke-width="3"/><g fill="#5a5a5a"><rect x="36" y="46" width="5" height="11"/><rect x="44" y="40" width="5" height="17"/><rect x="52" y="34" width="5" height="23"/></g></svg>
    <h3>Quality over quantity</h3><p>Proin iaculis purus consequat sem cure dignissim. Donec porttitor entum suscipit aenean rhoncus posuere elit in tincidunt.</p>
  </div>
  <div class="col" style="left:758px">
    <svg class="badge" viewBox="0 0 92 92"><circle cx="46" cy="46" r="42" fill="#fff" stroke="#5a5a5a" stroke-width="6"/><rect x="29" y="29" width="34" height="34" rx="3" fill="none" stroke="#5a5a5a" stroke-width="3"/><polyline points="33,56 41,45 48,50 58,36" fill="none" stroke="#5a5a5a" stroke-width="3.5"/></svg>
    <h3>Deliver excellence</h3><p>Proin iaculis purus consequat sem cure dignissim. Donec porttitor entum suscipit aenean rhoncus posuere elit in tincidunt.</p>
  </div>
</section>

<section class="call">
  <svg class="call-icon" viewBox="0 0 94 94" aria-hidden="true"><circle cx="47" cy="47" r="47" fill="#16a6ee"/><path d="M38 30c2-1 4 0 5 2l2 5c1 2 0 3-1 4l-2 2c1 4 4 8 8 10l2-2c1-1 3-1 4 0l4 3c2 1 2 3 1 5l-2 2c-2 2-6 2-9 0-7-4-12-10-15-17-1-4 0-8 3-10z" fill="#fff"/></svg>
  <h2>CALL</h2>
  <p class="call-number">02 9000 4821</p>
</section>

<section class="contact">
  <h2 class="section-title">CONTACT US</h2>
  <p class="section-sub">Lorem ipsum dolor sit amet</p>
  <div class="field name">Name</div>
  <div class="field email">Email</div>
  <div class="field message">Type your message...</div>
  <div class="send-btn">SEND</div>
</section>

<footer class="footer">
  <div class="brand">Brook &amp; Associates</div>
  <div class="social"><span></span><span></span></div>
</footer>

</body>
</html>
```